Catering Company Needs a Web Page Design

I already have my logo, and so I'm moving onto the next phase.. the web page design. Zestora is a gourmet catering company based in orlando, fl, set to launch in 2015. I will have a store location to host cooking classes as well.... and will be uploading cooking demo videos to my website weekly. Id like a blog section, and about, a video section, contact form, Services, Menu Samples..... My logo and concept is modern, innovative, and fun! I am targeting middle class to upper middle class women, but i want the site to be super unique.

Industry/Entity Type

Catering

Requirements
Must have
• The front/main page must have the logo... and the quillnote registry's definition of "zestora". I like movement... maybe the top banner can move somehow.. Im not a web designer, so i wont really know until I start seeing some examples. For now I dont have photos of my own cooking, so if you could use stock photos of catering dishes.. I uploaded a transparent logo also, maybe that could be the top banner placed over a scene of expertly plated hordourves...

```html
<!DOCTYPE html>
<html lang="en">
<head>
<meta charset="utf-8">
<title>Zestora – Gourmet Catering &amp; Cooking Classes</title>
<link href="https://fonts.googleapis.com/css2?family=Source+Sans+3:ital,wght@0,300;0,400;0,700;1,300;1,400&display=swap" rel="stylesheet">
<style>
  :root {
    --purple: #a714ee;
    --orange: #f29a0f;
    --ink: #1a1a1a;
    --logo-ink: #3a3a3a;
    --muted: #6b6b6b;
    --footer-bg: #5b5b5b;
    --footer-ink: #f2f2f2;
    --white: #ffffff;
  }
  * { margin: 0; padding: 0; box-sizing: border-box; }
  html, body { width: 914px; height: 1200px; overflow: hidden; background: var(--white); }
  body { font-family: "Source Sans 3", "Myriad Pro", sans-serif; color: var(--ink); position: relative; }

  .hero { position: absolute; left: 0; top: 0; width: 914px; height: 468px; overflow: hidden; }
  .hero-photo {
    position: absolute; inset: 0;
    background:
      radial-gradient(ellipse 60px 80px at 50px 270px, #6a2418 0%, #8a3a20 50%, transparent 100%),
      radial-gradient(ellipse 60px 80px at 225px 270px, #6a2418 0%, #8a3a20 50%, transparent 100%),
      radial-gradient(ellipse 60px 80px at 450px 270px, #6a2418 0%, #8a3a20 50%, transparent 100%),
      radial-gradient(ellipse 60px 80px at 675px 270px, #6a2418 0%, #8a3a20 50%, transparent 100%),
      linear-gradient(180deg, #f4f4f2 0%, #eceee6 36%, #a9c07a 46%, #98b46a 60%, #d7dccb 74%, #f0f0ec 88%, #f3f3f1 100%);
  }
  .brand { position: absolute; left: 58px; top: 46px; }
  .brand-name { font-weight: 700; font-size: 100px; line-height: 1; letter-spacing: -3px; color: var(--logo-ink); }
  .brand-tagline { margin: 4px 0 0 85px; font-weight: 400; font-size: 17px; color: var(--muted); letter-spacing: 0.3px; }

  .nav-tile {
    position: absolute; width: 94px; height: 186px; background: var(--purple);
    color: var(--ink); font-size: 70px; font-weight: 400; line-height: 1;
    display: flex; justify-content: center; padding-top: 56px;
    box-shadow: 3px 3px 4px rgba(0,0,0,0.35); text-decoration: none;
  }
  .nav-tile.t-a { left: 476px; top: 0; }
  .nav-tile.t-m { left: 587px; top: 0; }
  .nav-tile.t-b { left: 698px; top: 0; }
  .nav-tile.t-v { left: 806px; top: 0; }
  .nav-tile.t-c { left: 698px; top: 213px; }
  .nav-tile.t-s { left: 806px; top: 213px; }

  .definition { position: absolute; left: 52px; top: 412px; font-style: italic; font-weight: 300; font-size: 21px; color: var(--orange); }
  .definition-source { position: absolute; right: 114px; top: 442px; font-style: italic; font-weight: 300; font-size: 16px; color: var(--orange); }

  .intro-title { position: absolute; left: 52px; top: 530px; font-style: italic; font-weight: 300; font-size: 40px; color: var(--orange); }
  .mission { position: absolute; left: 52px; top: 600px; font-style: italic; font-weight: 300; font-size: 31px; line-height: 41.5px; color: var(--ink); }

  .video { position: absolute; left: 287px; top: 532px; width: 571px; height: 357px; background: #000; }
  .video-poster {
    position: absolute; left: 0; top: 0; width: 571px; height: 323px;
    background:
      radial-gradient(ellipse 160px 110px at 470px 110px, #4a2a1c 0%, #6b3d28 55%, transparent 100%),
      radial-gradient(ellipse 200px 120px at 260px 190px, #f1ece0 0%, #d9cfb6 40%, transparent 100%),
      radial-gradient(ellipse 140px 90px at 110px 250px, #c53624 0%, #7fae3c 60%, transparent 100%),
      linear-gradient(180deg, #6a6a6a 0%, #9a9a98 35%, #e8e8e6 75%, #f4f4f4 100%);
  }
  .video-controls { position: absolute; left: 0; bottom: 0; width: 571px; height: 34px; }
  .video-time { position: absolute; left: 358px; top: 10px; font-size: 11px; font-weight: 700; color: var(--white); }
  .video-title { position: absolute; left: 287px; width: 571px; top: 908px; text-align: center; font-style: italic; font-weight: 300; font-size: 21px; color: var(--orange); }

  .footer-rule { position: absolute; left: 0; top: 974px; width: 914px; height: 12px; background: var(--purple); }
  .site-footer { position: absolute; left: 0; top: 986px; width: 914px; height: 214px; background: var(--footer-bg); box-shadow: inset 0 6px 6px -3px rgba(0,0,0,0.45); }
  .footer-col { position: absolute; top: 40px; color: var(--footer-ink); font-weight: 300; }
  .footer-col h3 { font-weight: 300; font-size: 16px; margin-bottom: 20px; }
  .footer-col p { font-size: 16px; line-height: 20.6px; }
</style>
</head>
<body>
  <header class="hero">
    <div class="hero-photo" role="img" aria-label="Banner photo of plated hors d'oeuvres on white tasting spoons over a bed of green garnish"></div>
    <div class="brand">
      <div class="brand-name">zestora</div>
      <div class="brand-tagline">Gourmet Catering &amp; Cooking Classes</div>
    </div>
    <nav>
      <a class="nav-tile t-a" href="#about">a</a>
      <a class="nav-tile t-m" href="#menu">m</a>
      <a class="nav-tile t-b" href="#blog">b</a>
      <a class="nav-tile t-v" href="#videos">v</a>
      <a class="nav-tile t-c" href="#contact">c</a>
      <a class="nav-tile t-s" href="#services">s</a>
    </nav>
    <p class="definition">‘Those who are overly zealous and enthusiastic about eating, cooking, and fine dining’</p>
    <p class="definition-source">Quillnote Registry</p>
  </header>

  <main>
    <h1 class="intro-title">Catering</h1>
    <p class="mission">Mission state-<br>ment of zest-<br>ora. why we<br>are in busi-<br>ness and why<br>we entered<br>business</p>

    <div class="video">
      <div class="video-poster" role="img" aria-label="Video still of grilled beef, chicken and pepper skewers on a white plate"></div>
      <svg class="video-controls" width="571" height="34" viewBox="0 0 571 34">
        <rect x="0" y="0" width="571" height="34" fill="#000"/>
        <rect x="4" y="4" width="30" height="26" rx="3" fill="#1c1c1c"/>
        <path d="M15 10 L25 17 L15 24 Z" fill="#fff"/>
        <rect x="40" y="4" width="302" height="26" rx="3" fill="#1c1c1c"/>
        <rect x="47" y="14" width="288" height="6" fill="none" stroke="#ddd" stroke-width="1"/>
        <rect x="353" y="4" width="80" height="26" rx="3" fill="#111"/>
        <rect x="454" y="4" width="30" height="26" rx="3" fill="#1c1c1c"/>
        <path d="M462 14 h4 l5 -4 v14 l-5 -4 h-4 Z" fill="#fff"/>
        <path d="M474 13 q3 4 0 8" stroke="#fff" stroke-width="1.5" fill="none"/>
        <rect x="556" y="4" width="0" height="26" fill="#1c1c1c"/>
        <rect x="533" y="4" width="30" height="26" rx="3" fill="#1c1c1c"/>
        <path d="M541 11 h4 M541 11 v4 M555 11 h-4 M555 11 v4 M541 23 h4 M541 23 v-4 M555 23 h-4 M555 23 v-4" stroke="#fff" stroke-width="1.5"/>
        <rect x="544" y="14" width="8" height="6" fill="#fff"/>
      </svg>
      <span class="video-time">00:00 / 00:00</span>
    </div>
    <p class="video-title">Title for Hor-dourve Video</p>
  </main>

  <div class="footer-rule"></div>
  <footer class="site-footer">
    <div class="footer-col" style="left:57px"><h3>banquets</h3><p>this area<br>develops<br>as more info<br>is provided</p></div>
    <div class="footer-col" style="left:174px"><h3>&nbsp;&nbsp;&nbsp;menu</h3><p>this area<br>develops<br>as more info<br>is provided</p></div>
    <div class="footer-col" style="left:291px"><h3>classes</h3><p>this area<br>develops<br>as more info<br>is provided</p></div>
    <div class="footer-col" style="left:402px"><h3>schedule a meeting</h3><p>this area<br>develops<br>as more info<br>is provided</p></div>
    <div class="footer-col" style="left:610px"><h3>email sign up</h3><p>this area<br>develops<br>as more info<br>is provided</p></div>
    <div class="footer-col" style="left:762px"><h3>directions</h3><p>&nbsp;this area<br>&nbsp;develops<br>&nbsp;as more info<br>&nbsp;is provided</p></div>
  </footer>
</body>
</html>
```